Business Card Design for company

We want new business cards. We'd like something different-- yet still highly professional. Our tagline is Providing leadership, delivering success. Stock photos are ok, as long as they are relevant and look upscale.

Target Market(s)

Architecture/Business Management Consulting/Engineering Consulting

Contact Information for Business Card

dark gray background with pops of blue might be good, but you tell me. You're the designers. Rounded corners might be nice, but again, you tell me.

Font styles to use
Serif
Sans Serif

Colors
3276b5
5c5c5c
9d9d9d
fbfbfb

Requirements
Nice to have
• Something different, but still very professional.

```html
<!DOCTYPE html>
<html lang="en">
<head>
<meta charset="utf-8">
<title>Norvale Partners Business Cards</title>
<link rel="stylesheet" href="https://fonts.googleapis.com/css2?family=Montserrat:wght@400;600;700&family=Open+Sans:wght@400;600&display=swap">
<style>
  :root {
    --brand-blue: #3276b5;
    --deep-blue: #2c67a3;
    --ink-gray: #5c5c5c;
    --mid-gray: #9d9d9d;
    --paper: #fbfbfb;
    --slate-light: #7b828c;
    --slate-dark: #3c4148;
    --edge-gray: #4a4e55;
    --backdrop: #e9eaec;
  }
  * { box-sizing: border-box; margin: 0; padding: 0; }
  html, body {
    width: 1200px; height: 885px; overflow: hidden;
    background: var(--backdrop);
  }
  .canvas { position: relative; width: 1200px; height: 885px; }

  .card {
    position: absolute;
    width: 620px; height: 354px;
    border-radius: 4px;
    overflow: hidden;
    box-shadow: 0 10px 28px rgba(0,0,0,0.18);
  }

  /* Back of card */
  .card-back {
    left: 60px; top: 60px;
    background: linear-gradient(160deg, var(--slate-light) 0%, #5a6069 45%, var(--slate-dark) 100%);
    display: flex; flex-direction: column; align-items: center; justify-content: center;
  }
  .card-back .brand-name {
    font-family: "Montserrat", sans-serif;
    font-weight: 700;
    font-size: 54px;
    letter-spacing: 2px;
    color: var(--paper);
    margin-top: -20px;
  }
  .card-back .tagline {
    position: absolute; bottom: 60px; left: 0; right: 0;
    text-align: center;
    font-family: "Open Sans", sans-serif;
    font-size: 15px;
    color: var(--paper);
    letter-spacing: 0.3px;
  }
  .tagline .dot {
    display: inline-block; width: 6px; height: 6px; border-radius: 50%;
    background: var(--paper); margin: 0 10px; vertical-align: middle;
  }

  /* Front of card */
  .card-front {
    left: 520px; top: 470px;
    background: #ffffff;
  }
  .card-front .panel { position: absolute; inset: 0; }
  .card-front .brand-name {
    position: absolute; left: 34px; top: 62px;
    font-family: "Montserrat", sans-serif;
    font-weight: 700;
    font-size: 38px;
    line-height: 1.05;
    letter-spacing: 1px;
    color: var(--brand-blue);
  }
  .person { position: absolute; left: 34px; bottom: 34px; font-family: "Montserrat", sans-serif; }
  .person .name { font-weight: 700; font-size: 22px; color: var(--deep-blue); letter-spacing: 0.5px; }
  .person .title { font-weight: 400; font-size: 15px; color: var(--ink-gray); letter-spacing: 0.5px; }

  .contact {
    position: absolute; right: 22px; top: 116px;
    font-family: "Open Sans", sans-serif;
    color: var(--paper);
    text-align: right;
    font-size: 13px;
    line-height: 20px;
  }
  .contact .address { margin-bottom: 6px; }
  .contact li { list-style: none; display: flex; justify-content: flex-end; align-items: center; gap: 8px; white-space: nowrap; }
  .contact svg { width: 12px; height: 12px; fill: var(--paper); flex: none; }
</style>
</head>
<body>
<main class="canvas">

  <section class="card card-back" aria-label="Card back">
    <div class="brand-name">NORVALE</div>
    <p class="tagline">Providing leadership<span class="dot"></span>delivering success</p>
  </section>

  <section class="card card-front" aria-label="Card front">
    <svg class="panel" viewBox="0 0 620 354" width="620" height="354" aria-hidden="true">
      <polygon points="382,100 620,100 620,354 350,354 360,124" fill="var(--edge-gray)"/>
      <polygon points="390,100 620,100 620,354 358,354 368,124" fill="var(--brand-blue)"/>
    </svg>

    <div class="brand-name">NORVALE<br>PARTNERS</div>

    <div class="person">
      <div class="name">MARCUS HALE</div>
      <div class="title">PRESIDENT</div>
    </div>

    <ul class="contact">
      <li class="address">2170 Harborview Lane<br>Lake Ridge, NY 11020</li>
      <li>412 5580 1937
        <svg viewBox="0 0 16 16"><path d="M3 1l3 3-2 2c1 2 3 4 5 5l2-2 3 3-2 3C7 15 1 9 0 4z"/></svg></li>
      <li>731 2046 8819
        <svg viewBox="0 0 16 16"><path d="M4 0h8v16H4zM5.5 2v10h5V2zM7 13.5h2v1H7z"/></svg></li>
      <li>625 9187 4402
        <svg viewBox="0 0 16 16"><path d="M4 1h8v4h3v9H1V5h3zM5.5 2.5v3h5v-3zM3 8v4h10V8z"/></svg></li>
      <li>marcus@norvalepartners.com
        <svg viewBox="0 0 16 16"><path d="M0 3h16v10H0zM1.5 4.5l6.5 5 6.5-5v-.2H1.5z"/></svg></li>
      <li>www.norvalepartners.com
        <svg viewBox="0 0 16 16"><path d="M8 0a8 8 0 110 16A8 8 0 018 0zm-1 3H4.5A6 6 0 003 7h3zm2 0v4h4a6 6 0 00-1.5-4zM3 9a6 6 0 001.5 4H7V9zm6 0v4h2.5A6 6 0 0013 9z"/></svg></li>
    </ul>
  </section>

</main>
</body>
</html>
```